Employee I.D. Card - Badge

We need an employee I.D. card designed. Our employees are going to be wearing these. I would like to have it look nice. Something professional yet cool (not uptight if that makes sense).
Project Scope:
Vertical orientation
Company name ------------- (Bright and Tidy)
Website ------------- (brightandtidymn.example)
Employee Picture
background check image
front and back designed - same design on either side
You can create the card without having the employee images on them.
Here are the dimensions -
2.125 x 3.370 inches
Double sided - same design can be used front and back
Background badge - I would like to add an image that shows that the employee has taken a background check. I've added the press-kit for the company we use. If you have a better idea than incorporating their logo, we can certainly do something different.
Example image-
https://www.findwell-search.example/results?q=background+check+badge&mode=images
The print company will set up the names.
Logo is attached
Also attached are our business cards. You can use this for an idea of brand/company style.
Our website - brightandtidymn.example

```html
<!DOCTYPE html>
<html lang="en">
<head>
<meta charset="utf-8">
<title>Bright and Tidy — Employee ID Badge</title>
<link rel="stylesheet" href="https://fonts.googleapis.com/css2?family=Oswald:wght@500&family=Nunito:wght@700;800&display=swap">
<style>
  :root {
    --sky-light: #6fd0f7;
    --sky: #45b4f2;
    --band-blue: #3a9ff0;
    --lime: #b4e41c;
    --ink: #2b2b2b;
    --white: #ffffff;
    --bar-start: #2f8cf0;
    --bar-end: #2fe2fb;
    --brand-blue: #2b9fe6;
    --ghost: #eaf7fc;
    --portrait-dark: #2a2f4a;
    --portrait-warm: #6b4a3a;
  }
  * { margin: 0; padding: 0; box-sizing: border-box; }
  html, body {
    width: 769px; height: 1200px; overflow: hidden; background: var(--white);
  }
  .badge {
    position: relative; width: 769px; height: 1200px; overflow: hidden;
    background: var(--white);
  }
  .brand-ghost {
    position: absolute; top: 878px; left: 222px; width: 540px;
    font-family: "Nunito", sans-serif; font-weight: 800;
    font-size: 88px; line-height: 1.1; color: var(--ghost);
    letter-spacing: -2px; white-space: nowrap;
  }
  .badge-art { position: absolute; inset: 0; }
  .brand-name {
    position: absolute; top: 34px; right: 40px; width: 250px;
    font-family: "Nunito", sans-serif; font-weight: 800;
    font-size: 52px; line-height: 0.95; text-align: center;
    color: var(--brand-blue); letter-spacing: -1px;
  }
  .employee-name, .occupation {
    position: absolute; font-family: "Oswald", sans-serif; font-weight: 500;
    text-transform: uppercase; text-align: center;
  }
  .employee-name {
    left: 500px; width: 200px; top: 618px;
    font-size: 48px; line-height: 1.08; color: var(--white);
  }
  .occupation {
    left: 470px; width: 260px; top: 806px;
    font-size: 38px; line-height: 1; color: var(--ink);
  }
  .website {
    position: absolute; left: 194px; top: 1026px;
    font-family: "Nunito", sans-serif; font-weight: 800;
    font-size: 33px; color: var(--white); letter-spacing: 0.3px;
    white-space: nowrap;
  }
</style>
</head>
<body>
<main class="badge">
  <div class="brand-ghost" aria-hidden="true">Bright and<br>Tidy</div>

  <svg class="badge-art" width="769" height="1200" viewBox="0 0 769 1200">
    <defs>
      <linearGradient id="sky-fill" x1="0" y1="0" x2="0" y2="1">
        <stop offset="0" stop-color="var(--sky-light)"/>
        <stop offset="1" stop-color="var(--sky)"/>
      </linearGradient>
      <linearGradient id="bar-fill" x1="0" y1="0" x2="1" y2="0">
        <stop offset="0" stop-color="var(--bar-start)"/>
        <stop offset="1" stop-color="var(--bar-end)"/>
      </linearGradient>
      <linearGradient id="globe-fill" gradientUnits="userSpaceOnUse" x1="94" y1="1019" x2="154" y2="1079">
        <stop offset="0" stop-color="var(--bar-end)"/>
        <stop offset="1" stop-color="var(--bar-start)"/>
      </linearGradient>
      <linearGradient id="portrait-fill" x1="0" y1="0" x2="0" y2="1">
        <stop offset="0" stop-color="var(--portrait-warm)"/>
        <stop offset="1" stop-color="var(--portrait-dark)"/>
      </linearGradient>
      <clipPath id="above-diagonal">
        <polygon points="0,0 769,0 769,912 0,825"/>
      </clipPath>
    </defs>

    <g clip-path="url(#above-diagonal)">
      <rect class="sky" x="0" y="0" width="769" height="912" fill="url(#sky-fill)"/>
      <rect class="name-band" x="0" y="629" width="769" height="146" fill="var(--band-blue)"/>
      <ellipse class="portrait-backdrop" cx="160" cy="860" rx="290" ry="270" fill="var(--white)"/>
      <path class="portrait" role="img" aria-label="Employee portrait photo"
            d="M0,545 Q60,420 210,410 Q330,410 360,545 L400,700 Q470,740 475,860 L475,900 L0,900 Z"
            fill="url(#portrait-fill)"/>
    </g>

    <polygon class="occupation-band" points="405,775 769,775 769,912 472,877" fill="var(--lime)"/>

    <path class="brand-wave" d="M430,0 L769,0 L769,190 Q660,150 560,150 Q470,150 450,80 Q438,35 430,0 Z" fill="var(--white)"/>

    <circle cx="74" cy="570" r="9" fill="var(--white)"/>
    <circle cx="90" cy="564" r="5" fill="var(--white)"/>
    <circle cx="444" cy="665" r="8" fill="var(--white)"/>
    <circle cx="430" cy="672" r="4" fill="var(--white)"/>

    <g class="check-seal">
      <circle cx="388" cy="588" r="62" fill="var(--lime)"/>
      <circle cx="388" cy="588" r="48" fill="var(--white)"/>
      <circle cx="388" cy="588" r="28" fill="var(--lime)"/>
    </g>

    <rect class="web-bar" x="0" y="1013" width="769" height="72" fill="url(#bar-fill)"/>
    <circle cx="124" cy="1049" r="53" fill="var(--white)"/>
    <g class="globe-icon" fill="none" stroke="url(#globe-fill)" stroke-width="4">
      <circle cx="124" cy="1049" r="30"/>
      <ellipse cx="124" cy="1049" rx="13" ry="30"/>
      <line x1="94" y1="1049" x2="154" y2="1049"/>
      <line x1="99" y1="1034" x2="149" y2="1034"/>
      <line x1="99" y1="1064" x2="149" y2="1064"/>
      <line x1="124" y1="1019" x2="124" y2="1079"/>
    </g>
  </svg>

  <div class="brand-name">Bright and Tidy</div>
  <div class="employee-name">Employee<br>Name</div>
  <div class="occupation">Ocupation</div>
  <div class="website">brightandtidymn.example</div>
</main>
</body>
</html>
```